Aerospace Private Equity Firm Needs Website

We need a website for new private equity fund called Orlin Partners. We buy smaller companies in the aerospace and industrial industries. I have attached some information about the firm. An example of a site we like that is a similar business but focused in a different sector is www.travomedic.com. www.quarnestgrove.com is a firm that also invests in aerospace companies.

Industry/Entity Type

Equity

Number of Pages Required

1 page

Colors
0555a3
33a6d7
ec1f27

```html
<!DOCTYPE html>
<html lang="en">
<head>
<meta charset="utf-8">
<title>Orlin Partners</title>
<link rel="stylesheet" href="https://fonts.googleapis.com/css2?family=Montserrat:wght@400;500;600&display=swap">
<style>
:root{
  --navy:#0555a3;
  --sky:#33a6d7;
  --red:#ec1f27;
  --ink:#2b2b2b;
  --white:#ffffff;
  --card:rgba(62,104,134,0.78);
}
*{box-sizing:border-box;margin:0;padding:0}
html,body{width:1200px;height:1144px;overflow:hidden;background:var(--white)}
body{font-family:'Montserrat',sans-serif;color:var(--ink);position:relative}
.site-header{position:absolute;left:0;top:0;width:1200px;height:112px}
.brand{position:absolute;left:120px;top:36px;display:flex;align-items:center;gap:10px;color:var(--navy);font-weight:600;font-size:30px;letter-spacing:-0.5px}
.brand-mark{width:14px;height:14px;background:var(--navy)}
.login-btn{position:absolute;display:flex;align-items:center;gap:6px;color:var(--white);font-size:13px;text-transform:uppercase;text-decoration:none;border-radius:7px;padding:0 12px}
.login-btn svg{width:22px;height:22px}
.header-login{left:940px;top:38px;width:137px;height:36px;background:var(--sky)}
.main-nav{position:absolute;left:0;top:112px;width:1200px;height:51px;background:var(--sky);display:flex;justify-content:center;align-items:center}
.main-nav a{color:var(--white);text-decoration:none;font-size:13px;padding:0 21px;line-height:26px;border-left:2px dotted rgba(255,255,255,0.9)}
.main-nav a:first-child{border-left:none}
.hero{position:absolute;left:0;top:163px;width:1200px;height:583px;background:linear-gradient(180deg,#a4a6a4 0%,#8d9195 30%,#6c7278 55%,#3e4348 78%,#4a4f55 100%)}
.hero-card{position:absolute;background:var(--card);color:var(--white);padding:12px 15px 0 17px}
.hero-card .num{font-size:19px;padding-bottom:10px;border-bottom:1px solid rgba(255,255,255,0.8);margin-bottom:13px}
.hero-card h3{font-size:13.5px;font-weight:600;text-transform:uppercase;margin-bottom:6px}
.hero-card p{font-size:11px;line-height:19px}
.card-1{left:118px;top:423px;width:279px;height:158px}
.card-2{left:455px;top:492px;width:279px;height:90px}
.card-3{left:798px;top:492px;width:279px;height:90px}
.intro{position:absolute;left:120px;top:783px;width:600px}
.section-title{font-size:29px;font-weight:600;color:var(--ink)}
.section-title span{color:var(--sky)}
.intro .section-title{padding-left:5px}
.intro p{margin-top:20px;font-size:14.5px;line-height:24px}
.services{position:absolute;left:790px;top:781px;width:288px}
.services ul{list-style:none;margin-top:18px;padding-left:5px}
.services li{font-size:16px;line-height:23px;padding:3px 0 3px;border-bottom:1px dashed #c8e3f1;height:31px}
.site-footer{position:absolute;left:0;top:1052px;width:1200px;height:92px;background:var(--sky);color:var(--white)}
.footer-login{left:115px;top:29px;width:140px;height:38px;border:2px solid var(--white);border-radius:9px}
.legal{position:absolute;left:278px;top:38px;font-size:14.5px}
.legal a{color:var(--white);text-decoration:none}
.copyright{position:absolute;right:122px;top:38px;font-size:14.5px}
</style>
</head>
<body>
<header class="site-header">
  <div class="brand"><span class="brand-mark"></span>Orlin Partners</div>
  <a class="login-btn header-login" href="#">Client Login
    <svg viewBox="0 0 24 24" fill="none" stroke="#fff" stroke-width="1.5"><path d="M9 3h11v18H9v-4"/><path d="M9 7V3"/><path d="M15 12H3m4-4-4 4 4 4"/></svg>
  </a>
</header>
<nav class="main-nav">
  <a href="#">HOME</a><a href="#">TEAM</a><a href="#">INVESTMENT</a><a href="#">STRATEGY</a><a href="#">ABOUT</a><a href="#">CONTACT US</a>
</nav>
<section class="hero" role="img" aria-label="Fighter jets parked on an airfield apron at dusk with mountains behind">
  <div class="hero-card card-1">
    <div class="num">01</div>
    <h3>Aenean convallis ipsum</h3>
    <p>Nulla facilisi. Aliquam vestibulum felis a congue tincidunt. Vestibulum vel hendrerit justo. Sed rhoncus ornare enim ac facilisis.</p>
  </div>
  <div class="hero-card card-2">
    <div class="num">02</div>
    <h3>Mauris efficitur eget</h3>
  </div>
  <div class="hero-card card-3">
    <div class="num">03</div>
    <h3>Suspendisse non tempor</h3>
  </div>
</section>
<section class="intro">
  <h2 class="section-title">Lorem ipsum <span>Dolor Amet</span></h2>
  <p>Nunc imperdiet massa erat. Sed finibus commodo purus eu feugiat. Mauris rhoncus nibh eu commodo viverra. Aliquam ac venenatis metus, at dignissim nulla. Ut venenatis turpis sed eros semper hendrerit. Mauris mattis erat non massa pharetra, sit amet feugiat est cursus. Curabitur hendrerit finibus turpis, placerat cursus metus suscipit vulputate. Nulla nisi lorem, tincidunt sodales sapien eget, commodo molestie ex.</p>
</section>
<section class="services">
  <h2 class="section-title">Our <span>Services</span></h2>
  <ul>
    <li>·Ulla sed</li>
    <li>·Maximus</li>
    <li>·Aliquam</li>
    <li>·Tempus</li>
    <li>·Etus a aucto</li>
  </ul>
</section>
<footer class="site-footer">
  <a class="login-btn footer-login" href="#">Client Login
    <svg viewBox="0 0 24 24" fill="none" stroke="#fff" stroke-width="1.5"><path d="M9 3h11v18H9v-4"/><path d="M9 7V3"/><path d="M15 12H3m4-4-4 4 4 4"/></svg>
  </a>
  <div class="legal"><a href="#">Legal Disclaimer</a> | <a href="#">User Agreement</a></div>
  <div class="copyright">Copyright © 2017 Orlin. All Rights Reserved.</div>
</footer>
</body>
</html>
```